NEW Website DESIGN for Brightfold Panes & Worktops Company

Brand New website, contemporary, clean, visual (images), not busy. ATTACHED IS OUR LOG THAT YOU MUST USE.

The company is called Brightfold Panes & Worktops (BrightfoldPW)
www.brightfoldpw.com
The website should be www.brightfoldpnw.com
one page for glass one page for solid surfaces www.brightfoldpanesplashes.co.uk
www.brightfoldpanesworktops.co.uk

Target Market(s)

Hotels, Commercial projects, Small focus on residential

Industry/Entity Type

Construction

Number of Pages Required

5+ page

Font styles to use
Sans Serif

Requirements
Must have
• COLOURS AS PER OUR LOGO - WHITE/YELLOW/GREY - WHITE BACK GROUND
• CLEAR SIMPLE NAVIGATION - MODER CLEAN CUT - DESIGN FEEL
• LATEST NAVIGATION FOR IMAGES and text to include per project details
• WORK/PROJECT AREA - NEWS AREA - TEAM AREA/ABOUT US/CONTACT US
• NEW PAGEwww.brightfoldpanesplashes.co.uk - NEW PAGE www.brightfoldpanesworktops.co.uk
• PLEASE COPY THIS TYPE OF TEMPALTE
• https://www.velmarbuild.co.uk/project/grand-suites/
• MOBILE READY
• WORDPRESS
• MODERN IMAGES INCLUDING LUMERAX HALVERN AND GLASS PROJECTS
Nice to have
• NEW DESIGN MODER FRESH
• WEBSITES I LIKE THE TEMPLATE SHOULD BE LIKE THE WEBSITE BELOW
• https://www.velmarbuild.co.uk/
Should not have
• NOT Old fashion template, not busy NAVIGATION
• NO BLACK
• NO DARK GREYS
• NOT LOTS OF YELLOW
• RESDENTIAL IMAGES

```html
<!DOCTYPE html>
<html lang="en">
<head>
<meta charset="utf-8">
<title>Brightfold Panes &amp; Worktops — Home</title>
<link rel="stylesheet" href="https://fonts.googleapis.com/css2?family=Cormorant+Garamond:wght@500;600&family=Montserrat:wght@500&display=swap">
<style>
  :root{
    --stage:#dcdcdc;
    --white:#ffffff;
    --grey:#858585;
    --grey-footer:#8a8a8a;
    --grey-bar:#6f6f6f;
    --yellow:#d9d21c;
    --ink:#6b6b6b;
    --serif:"Cormorant Garamond", Georgia, serif;
    --sans:"Montserrat", Arial, sans-serif;
  }
  *{box-sizing:border-box;margin:0;padding:0}
  html,body{width:1200px;height:800px;overflow:hidden;background:var(--stage)}
  .canvas{position:relative;width:1200px;height:800px}
  .page{
    position:absolute;left:477px;top:9px;width:293px;height:930px;
    background:var(--white);transform:scale(.84);transform-origin:0 0;
    font-family:var(--serif);color:var(--ink);
  }
  .page > *{position:absolute}
  /* header */
  .brand{left:16px;top:8px;display:flex;flex-direction:column;align-items:center;gap:3px}
  .brand-dot{width:20px;height:20px;border-radius:50%;background:var(--grey)}
  .brand-name{font-family:var(--sans);font-size:4px;color:var(--ink);letter-spacing:.1px}
  .hero{left:0;top:37px;width:293px;height:187px;
    background:linear-gradient(180deg,#d9d3cf 0%,#efe9e7 35%,#c9b9a6 55%,#6b5443 78%,#3f3128 100%)}
  .nav{left:0;top:224px;width:293px;height:15px;background:var(--grey);
    display:flex;justify-content:flex-end;align-items:center;gap:11px;padding-right:10px;
    list-style:none;font-size:3px;color:var(--yellow)}
  /* section headings */
  .heading{font-size:5px;color:var(--yellow);letter-spacing:.3px;text-transform:uppercase;
    border-bottom:.5px solid var(--yellow);padding-bottom:1px;left:0;width:293px;text-align:center;border:none}
  .heading span{border-bottom:.5px solid var(--yellow);padding-bottom:1px}
  /* about */
  .about-photo{left:20px;top:265px;width:124px;height:83px;
    background:linear-gradient(135deg,#2d3a3c,#6f7c78 50%,#3a2e2a)}
  .about-title{left:165px;top:270px;font-size:4.5px;color:var(--yellow)}
  .about-text{left:150px;top:279px;width:122px;font-size:3.1px;line-height:1.45;text-align:right}
  .btn{background:var(--grey);display:block}
  .about-btn{left:166px;top:334px;width:35px;height:11px}
  /* projects */
  .project{top:423px;width:58px;height:58px}
  /* blog */
  .blog{left:20px;top:524px;width:252px;height:92px;display:grid;
    grid-template-columns:repeat(4,1fr);grid-template-rows:1fr 1fr;gap:2px}
  .blog-card{background:var(--grey);display:flex;flex-direction:column;align-items:center;justify-content:center;gap:8px}
  .blog-card p{font-size:3.2px;color:var(--yellow)}
  .blog-more{background:var(--white);font-size:2.4px;color:var(--grey);padding:1.5px 5px}
  .blog-photo{background:linear-gradient(180deg,#cfd6d8,#8e989a 60%,#55605f)}
  /* team */
  .team{left:20px;top:665px;width:252px;height:101px;background:var(--grey);
    display:flex;flex-direction:column;align-items:center;padding-top:14px;color:var(--white);font-size:3.6px;line-height:2.7}
  .avatar{width:40px;height:40px;border-radius:50%;background:linear-gradient(160deg,#e8eef2,#b9c6cf);margin-bottom:4px}
  /* contact */
  .field{top:814px;height:19px;background:var(--grey);color:var(--white);font-size:3.6px;
    display:flex;align-items:center;justify-content:center;letter-spacing:.3px}
  /* footer */
  .footer{left:0;top:862px;width:293px;height:86px;background:var(--grey-footer);
    display:grid;grid-template-columns:62px 64px 73px 1fr;padding:14px 10px 0 22px;font-size:3.1px;line-height:1.55;color:var(--white)}
  .footer h4{font-weight:500;font-size:3.4px;margin-bottom:3px;letter-spacing:.2px}
  .footer .links{color:var(--yellow);list-style:none;line-height:3.4}
  .footer .mail{color:var(--yellow)}
  .gallery{display:grid;grid-template-columns:1fr 1fr;gap:1px;width:42px}
  .gallery i{display:block;height:26px;background:linear-gradient(160deg,#dfe5e8,#7b8790)}
  .copyright{left:0;top:948px;width:293px;height:19px;background:var(--grey-bar);color:var(--white);
    font-size:2.8px;display:flex;align-items:center;justify-content:center}
</style>
</head>
<body>
<div class="canvas">
  <main class="page">
    <header class="brand">
      <span class="brand-dot"></span>
      <span class="brand-name">Brightfold Panes &amp; Worktops</span>
    </header>
    <div class="hero" role="img" aria-label="Photo of a bright glass-walled boardroom with a long table and leather chairs"></div>
    <ul class="nav"><li>Home</li><li>About Us</li><li>Project</li><li>Blog</li><li>Team</li><li>Contact Us</li></ul>

    <div class="about-photo" role="img" aria-label="Photo of a glass-fronted building entrance"></div>
    <h2 class="about-title">ABOUT US</h2>
    <p class="about-text">Lorem ipsum is simply dummy text of the print and typesetting industry. Lorem ipsum has been the standard dummy text ever since the 1500s, when an unknown printer took a galley of type and scrambled it to make a type specimen book. It has survived not only five centuries, but also the leap into electronic typesetting, remaining essentially unchanged. Lorem ipsum is simply dummy text of the print and typesetting industry.</p>
    <span class="btn about-btn"></span>

    <h2 class="heading" style="top:409px"><span>OUR PROJECT</span></h2>
    <div class="project" style="left:20px;width:81px;background:linear-gradient(180deg,#1e3a6e,#2c3f6a 55%,#5a4530)" role="img" aria-label="Photo of a lit house at dusk"></div>
    <div class="project" style="left:106px;width:81px;background:linear-gradient(135deg,#2b5a78,#8fb4c8 50%,#355a70)" role="img" aria-label="Photo of glass tower facades"></div>
    <div class="project" style="left:191px;width:81px;background:linear-gradient(135deg,#2a2a2a,#d8d8d8 50%,#5a5a5a)" role="img" aria-label="Black and white photo of glass skyscrapers"></div>

    <h2 class="heading" style="top:503px"><span>LATEST BLOG</span></h2>
    <section class="blog">
      <div class="blog-card"><p>Lorem Ipsum has been the</p><span class="blog-more">KNOW MORE</span></div>
      <div class="blog-photo" role="img" aria-label="Photo of a glass office interior"></div>
      <div class="blog-card"><p>Lorem Ipsum has been the</p><span class="blog-more">KNOW MORE</span></div>
      <div class="blog-photo" role="img" aria-label="Photo of a glass office interior"></div>
      <div class="blog-photo" role="img" aria-label="Photo of a glass office interior"></div>
      <div class="blog-card"><p>Lorem Ipsum has been the</p><span class="blog-more">KNOW MORE</span></div>
      <div class="blog-photo" role="img" aria-label="Photo of a glass office interior"></div>
      <div class="blog-card"><p>Lorem Ipsum has been the</p><span class="blog-more">KNOW MORE</span></div>
    </section>

    <h2 class="heading" style="top:641px"><span>OUR TEAM</span></h2>
    <section class="team">
      <div class="avatar" role="img" aria-label="Team member portrait"></div>
      <p>Lorem Ipsum is simply dummy text of the printing and typesetting</p>
      <p style="line-height:1">Lorem Ipsum is simply dummy text of the printing and typesetting</p>
    </section>

    <h2 class="heading" style="top:791px"><span>CONTACT US</span></h2>
    <div class="field" style="left:42px;width:145px">ENTER YPOUR EMAIL ID</div>
    <div class="field" style="left:191px;width:60px">SEND</div>

    <footer class="footer">
      <div>
        <h4>ABOUT US</h4>
        <p style="text-align:right;padding-right:6px">Lorem Ipsum is simply dummy text of the printing and typesetting industry. Lorem Ipsum has been the industry's standard dummy text ever since the 1500s, when an unknown printer took a galley of type and</p>
      </div>
      <div>
        <h4>SOLUTIONS</h4>
        <ul class="links"><li>Lorem Ipsum is simply</li><li>Lorem Ipsum is simply</li><li>Lorem Ipsum is simply</li><li>Lorem Ipsum is simply</li><li>Lorem Ipsum is simply</li></ul>
      </div>
      <div>
        <h4>CONTACT US</h4>
        <p>4720 Ridge Block, Harlow Central, Island</p>
        <p style="margin-top:3px">+441 555 0182 7730</p>
        <p class="mail" style="margin-top:3px">CONTACT @ MAILBOX.COM</p>
        <p class="mail" style="margin-top:3px">WEBSITE @ SITENET.COM</p>
      </div>
      <div>
        <h4>GALLERY POSTS</h4>
        <div class="gallery"><i role="img" aria-label="Recent project photo"></i><i role="img" aria-label="Recent project photo"></i><i role="img" aria-label="Recent project photo"></i><i role="img" aria-label="Recent project photo"></i></div>
      </div>
    </footer>
    <div class="copyright">COPYRIGHT 2018</div>
  </main>
</div>
</body>
</html>
```